Music Quizz Application

Hello,

I want a new design for my Blind test (music quizz) application on Velbix. You will find attached the images I want to replace. I need something with the same element (menu / song title) but with a different look!

Same, new icon, you have carte blanche to this one.

I am looking for something fresh…. I'm looking for something with a real artistic choice, contrast, colours, etc.

As a marketing screenshot, I want something classic, you'll find an example attached, feel free to innovate.

To sum-up :

- One new view for my App
- One new icon
- One marketing screenshot

screen resolution :
640×960
icon resolution :
1024x1024

Target Market(s)

15-30 years

Industry/Entity Type

Marketing

```html
<!DOCTYPE html>
<html lang="en">
<head>
<meta charset="utf-8">
<title>Tunebound – Velbix app screens</title>
<link rel="stylesheet" href="https://fonts.googleapis.com/css2?family=Ubuntu:wght@400;500;700&family=Roboto:wght@400;500&display=swap">
<style>
  :root {
    --page-bg: #e6e6e6;
    --page-bg-edge: #cfcfcf;
    --screen-black: #0b0b0b;
    --status-text: #e8e8e8;
    --panel-bg: rgba(22, 22, 22, 0.82);
    --panel-border: rgba(255, 255, 255, 0.14);
    --divider: rgba(255, 255, 255, 0.12);
    --text-light: #f2f2f2;
    --text-muted: #cfcfcf;
    --brand-ink: #161616;
    --bokeh-teal: #4fc9a8;
    --bokeh-green: #6f9a52;
    --bokeh-amber: #e3a04a;
    --bokeh-rust: #b6502e;
    --bokeh-cream: #fbf2dc;
  }
  * { box-sizing: border-box; margin: 0; padding: 0; }
  html, body { width: 1200px; height: 800px; overflow: hidden; }
  body {
    background: radial-gradient(ellipse at 50% 40%, var(--page-bg) 0%, var(--page-bg) 45%, var(--page-bg-edge) 100%);
    font-family: "Roboto", Arial, sans-serif;
    position: relative;
  }
  .screen-row {
    position: absolute;
    left: 60px; top: 160px;
    display: flex; gap: 60px;
  }
  .screen {
    position: relative;
    width: 320px; height: 480px;
    background: var(--screen-black);
    overflow: hidden;
    box-shadow: 0 14px 30px rgba(0,0,0,0.25);
  }
  .status-bar {
    position: absolute; left: 0; top: 0; right: 0; height: 20px;
    background: #000;
    color: var(--status-text);
    font-size: 11px; font-weight: 500;
    display: flex; align-items: center; justify-content: space-between;
    padding: 0 6px; z-index: 2;
  }
  .status-left, .status-right { display: flex; align-items: center; gap: 5px; }
  .status-time { position: absolute; left: 50%; transform: translateX(-50%); }
  .bokeh {
    position: absolute; left: 0; top: 20px; right: 0; bottom: 0;
    background:
      radial-gradient(circle at 52% 40%, var(--bokeh-cream) 0%, rgba(251,242,220,0.7) 16%, rgba(251,242,220,0) 40%),
      radial-gradient(circle at 12% 32%, var(--bokeh-teal) 0%, rgba(79,201,168,0) 30%),
      radial-gradient(circle at 85% 22%, var(--bokeh-amber) 0%, rgba(227,160,74,0) 32%),
      radial-gradient(circle at 95% 10%, var(--bokeh-rust) 0%, rgba(182,80,46,0) 25%),
      radial-gradient(circle at 20% 62%, var(--bokeh-green) 0%, rgba(111,154,82,0) 34%),
      radial-gradient(circle at 70% 70%, rgba(120,110,70,0.7) 0%, rgba(0,0,0,0) 35%),
      linear-gradient(180deg, #2c2a24 0%, #1c1c18 60%, #0e0e0c 100%);
  }
  .bokeh.is-dim::after {
    content: ""; position: absolute; inset: 0;
    background: rgba(0,0,0,0.28);
  }
  .brand {
    position: absolute; left: 0; right: 0;
    display: flex; flex-direction: column; align-items: center;
    z-index: 1;
  }
  .brand-dot {
    width: 86px; height: 86px; border-radius: 50%;
    border: 4px solid var(--brand-ink);
  }
  .brand-name {
    margin-top: 14px;
    font-family: "Ubuntu", sans-serif;
    font-weight: 500; font-size: 40px; letter-spacing: -0.5px;
    color: var(--brand-ink);
  }
  .panel {
    position: absolute;
    background: var(--panel-bg);
    border: 1px solid var(--panel-border);
    border-radius: 3px;
    color: var(--text-light);
    z-index: 1;
    box-shadow: 0 2px 8px rgba(0,0,0,0.4);
  }
  .score-help { left: 52px; top: 283px; width: 216px; height: 188px; padding: 0 10px; }
  .score-help h2 {
    font-size: 11.5px; font-weight: 500; text-align: center;
    padding: 8px 0 7px; border-bottom: 1px solid var(--divider);
  }
  .score-help p { font-size: 10px; line-height: 1.35; color: var(--text-muted); margin-top: 7px; }
  .main-menu { left: 63px; top: 305px; width: 194px; padding: 0 10px; }
  .menu-item {
    display: block; height: 34px; line-height: 34px;
    text-align: center; font-size: 11px; font-weight: 500;
    border-bottom: 1px solid var(--divider);
  }
  .menu-item:last-child { border-bottom: none; }
  .test-button {
    left: 55px; top: 40px; width: 210px; height: 30px; line-height: 28px;
    text-align: center; font-size: 11.5px; font-weight: 500;
  }
  .song-list { left: 45px; top: 86px; width: 230px; list-style: none; padding: 0 8px; }
  .song-list li {
    height: 40px; line-height: 40px; text-align: center;
    font-size: 11px; border-bottom: 1px solid var(--divider);
    white-space: nowrap; overflow: hidden;
  }
  .song-list li:last-child { border-bottom: none; }
</style>
</head>
<body>
<main class="screen-row">

  <section class="screen screen-score-help" aria-label="Score rules screen">
    <header class="status-bar">
      <span class="status-left">
        <svg width="18" height="8" viewBox="0 0 18 8" aria-hidden="true"><g fill="#e8e8e8"><rect x="0" y="6" width="2" height="2"/><rect x="4" y="4" width="2" height="4"/><rect x="8" y="2" width="2" height="6"/><rect x="12" y="0" width="2" height="8" opacity=".4"/></g></svg>
        NEXA 3G</span>
      <span class="status-time">12:14</span>
      <span class="status-right">89 %
        <svg width="22" height="10" viewBox="0 0 22 10" aria-hidden="true"><rect x=".5" y=".5" width="18" height="9" rx="1.5" fill="none" stroke="#e8e8e8"/><rect x="2" y="2" width="15" height="6" fill="#e8e8e8"/><rect x="19.5" y="3" width="2" height="4" fill="#e8e8e8"/></svg></span>
    </header>
    <div class="bokeh is-dim" role="img" aria-label="Blurred colourful concert lights background"></div>
    <div class="brand" style="top:86px">
      <span class="brand-dot"></span>
      <span class="brand-name">Tunebound</span>
    </div>
    <article class="panel score-help">
      <h2>How the score is calculated?</h2>
      <p>Points are awarded as follows:</p>
      <p>-1 for each incorrect answer</p>
      <p>+5 or +10 for each correct answer (depending upon whether your game features 5 or 10 possible answers)</p>
      <p>1 point deducted for every 10 seconds that pass.</p>
    </article>
  </section>

  <section class="screen screen-main-menu" aria-label="Main menu screen">
    <header class="status-bar">
      <span class="status-left">
        <svg width="18" height="8" viewBox="0 0 18 8" aria-hidden="true"><g fill="#e8e8e8"><rect x="0" y="6" width="2" height="2"/><rect x="4" y="4" width="2" height="4"/><rect x="8" y="2" width="2" height="6"/><rect x="12" y="0" width="2" height="8" opacity=".4"/></g></svg>
        NEXA 3G</span>
      <span class="status-time">12:14</span>
      <span class="status-right">89 %
        <svg width="22" height="10" viewBox="0 0 22 10" aria-hidden="true"><rect x=".5" y=".5" width="18" height="9" rx="1.5" fill="none" stroke="#e8e8e8"/><rect x="2" y="2" width="15" height="6" fill="#e8e8e8"/><rect x="19.5" y="3" width="2" height="4" fill="#e8e8e8"/></svg></span>
    </header>
    <div class="bokeh" role="img" aria-label="Blurred colourful concert lights background"></div>
    <div class="brand" style="top:100px">
      <span class="brand-dot"></span>
      <span class="brand-name">Tunebound</span>
    </div>
    <nav class="panel main-menu">
      <a class="menu-item">Quick Game</a>
      <a class="menu-item">Blind Test</a>
      <a class="menu-item">Challenge</a>
    </nav>
  </section>

  <section class="screen screen-song-list" aria-label="Song list screen">
    <header class="status-bar">
      <span class="status-left">
        <svg width="18" height="8" viewBox="0 0 18 8" aria-hidden="true"><g fill="#e8e8e8"><rect x="0" y="6" width="2" height="2"/><rect x="4" y="4" width="2" height="4"/><rect x="8" y="2" width="2" height="6"/><rect x="12" y="0" width="2" height="8" opacity=".4"/></g></svg>
        NEXA 3G</span>
      <span class="status-time">12:14</span>
      <span class="status-right">89 %
        <svg width="22" height="10" viewBox="0 0 22 10" aria-hidden="true"><rect x=".5" y=".5" width="18" height="9" rx="1.5" fill="none" stroke="#e8e8e8"/><rect x="2" y="2" width="15" height="6" fill="#e8e8e8"/><rect x="19.5" y="3" width="2" height="4" fill="#e8e8e8"/></svg></span>
    </header>
    <div class="bokeh is-dim" role="img" aria-label="Blurred colourful concert lights background"></div>
    <div class="panel test-button">Test Button</div>
    <ul class="panel song-list">
      <li>Marcher sous l'orage</li>
      <li>Nora</li>
      <li>Les trois rives</li>
      <li>Reviens-moi</li>
      <li>Beau dimanche</li>
      <li>Lueur d'été (version 2009)</li>
      <li>Drifting Alone</li>
      <li>Écris-moi</li>
      <li>Les saisons</li>
    </ul>
  </section>

</main>
</body>
</html>
```